Home inspection business! professional look attracting customers just by looks. Read must haves

its a new business I started on my own for home inspections I would like something very professional to give to real estate agents and clients, its going to have my license number on it my business phone number my name my website as well etc on the back side it will be servicing areas and also what kind of services I offer I also have a business card from someone else the way I would like mine to be. I will attach my logo

Home Inspection

listed in nice to haves

• phone number - 555 293 8471
• website- hollowpinecheck.com
• license number #2938475610
• my name Gavin keropulis
• picture of my logo and me on the front
• on the back of the card. stating I am servicing All of New York and Long Island
• also services I will offer will be home inspection -mold inspection -lead inspection -radon inspection -Termite Inspection -Infared Scan.
• and also we provide inspections for single family homes condos co-ops town-homes
• and commercial property
• same colors as the logos and also if you recommend fonts to look like the logo not sure up to you

```html
<!DOCTYPE html>
<html lang="en">
<head>
<meta charset="utf-8">
<title>HollowPine Home Inspectors – Business Card</title>
<link rel="stylesheet" href="https://fonts.googleapis.com/css2?family=Poppins:wght@300;400;500;600;700&display=swap">
<style>
  :root {
    --blue: #4a9ede;
    --blue-bright: #52a6e0;
    --grey: #6f6f6f;
    --ink: #6b6b6b;
    --white: #ffffff;
    --stage: #2b2b2d;
  }
  * { box-sizing: border-box; margin: 0; padding: 0; }
  html, body { width: 1200px; height: 900px; overflow: hidden; }
  body {
    background: var(--stage);
    font-family: "Poppins", sans-serif;
    display: flex;
    flex-direction: column;
    align-items: center;
    justify-content: center;
    gap: 34px;
  }
  .card {
    position: relative;
    width: 700px;
    height: 400px;
    overflow: hidden;
    box-shadow: 0 10px 28px rgba(0,0,0,.45);
  }

  /* ---------- front ---------- */
  .card--front { background: var(--white); }
  .brand {
    position: absolute;
    display: flex;
    align-items: center;
    gap: 14px;
  }
  .brand__dot {
    width: 46px; height: 46px;
    border-radius: 50%;
    background: currentColor;
    flex: none;
  }
  .brand__name {
    font-weight: 600;
    line-height: 1.1;
    letter-spacing: .5px;
  }
  .brand__name span { display: block; font-size: .52em; letter-spacing: 7px; margin-top: 4px; }
  .card--front .brand { left: 44px; top: 52px; color: var(--grey); }
  .card--front .brand__name { font-size: 34px; }
  .front__rule {
    position: absolute;
    left: 0; right: 0; top: 238px;
    height: 4px;
    background: var(--blue);
  }
  .portrait {
    position: absolute;
    right: 46px; top: 58px;
    width: 140px; height: 160px;
    border: 1px solid #9a9a9a;
    background: linear-gradient(160deg, #f4f1ee 0%, #d9c2ad 45%, #3b3b42 100%);
  }
  .person {
    position: absolute;
    right: 206px; top: 146px;
    text-align: right;
  }
  .person__name { font-size: 25px; font-weight: 600; color: var(--ink); line-height: 1.3; }
  .person__role { font-size: 17px; font-weight: 400; color: var(--blue); margin-top: 6px; line-height: 1.3; }
  .license {
    position: absolute;
    left: 44px; top: 262px;
    font-size: 16px; font-weight: 300; color: var(--ink);
  }
  .contacts {
    position: absolute;
    right: 46px; bottom: 40px;
    list-style: none;
    font-size: 17px; font-weight: 400; color: var(--ink);
  }
  .contacts li {
    display: flex; align-items: center; justify-content: flex-end;
    gap: 10px; margin-top: 8px;
  }
  .contacts svg { width: 22px; height: 22px; flex: none; }

  /* ---------- back ---------- */
  .card--back {
    background: linear-gradient(110deg, var(--grey) 0%, #7d8a96 40%, var(--blue-bright) 100%);
    color: var(--white);
  }
  .card--back .brand {
    left: 50%; top: 38px;
    transform: translateX(-50%);
    color: var(--white);
  }
  .card--back .brand__name { font-size: 30px; }
  .area-band {
    position: absolute;
    left: 0; right: 0; top: 152px;
    height: 40px;
    background: var(--white);
    color: var(--blue);
    font-size: 17px; font-weight: 600;
    text-transform: uppercase;
    display: flex; align-items: center; justify-content: center;
    letter-spacing: .3px;
  }
  .services {
    position: absolute;
    left: 0; right: 0; top: 210px;
    text-align: center;
    font-size: 16px; font-weight: 400;
    line-height: 1.65;
  }
  .services__sep {
    display: inline-block;
    width: 6px; height: 6px;
    border-radius: 50%;
    background: var(--white);
    margin: 0 8px;
    vertical-align: middle;
  }
  .services__dash {
    width: 26px; height: 2px;
    background: var(--white);
    margin: 6px auto 8px;
  }
</style>
</head>
<body>

  <section class="card card--front" aria-label="Business card front">
    <div class="brand">
      <div class="brand__dot"></div>
      <div class="brand__name">HOLLOWPINE<span>HOME INSPECTORS</span></div>
    </div>
    <div class="portrait" role="img" aria-label="Portrait photo of Gavin keropulis"></div>
    <div class="person">
      <p class="person__name">Gavin keropulis</p>
      <p class="person__role">Managing Derector</p>
    </div>
    <div class="front__rule"></div>
    <p class="license">license number #2938475610</p>
    <ul class="contacts">
      <li>555 293 8471
        <svg viewBox="0 0 24 24" aria-hidden="true"><circle cx="12" cy="12" r="12" fill="#4a9ede"/><path d="M9.2 6.5c.4 0 .7.2.8.6l.6 1.8c.1.4 0 .7-.3.9l-.9.7c.6 1.3 1.7 2.4 3 3l.7-.9c.2-.3.6-.4.9-.3l1.8.6c.4.1.6.4.6.8v1.6c0 .5-.4.9-.9.9C10.4 16.2 7.8 13.6 7.6 8.3c0-.5.4-.9.9-.9z" fill="#fff"/></svg>
      </li>
      <li>www.hollowpinecheck.com
        <svg viewBox="0 0 24 24" aria-hidden="true"><circle cx="12" cy="12" r="12" fill="#4a9ede"/><rect x="6.5" y="8" width="11" height="8" rx="1" fill="#fff"/><path d="M6.8 8.4 12 12.3l5.2-3.9" fill="none" stroke="#4a9ede" stroke-width="1.2"/></svg>
      </li>
    </ul>
  </section>

  <section class="card card--back" aria-label="Business card back">
    <div class="brand">
      <div class="brand__dot"></div>
      <div class="brand__name">HOLLOWPINE<span>HOME INSPECTORS</span></div>
    </div>
    <div class="area-band">I am servicing all of New York and Long Island</div>
    <div class="services">
      <p>Home inspection<span class="services__sep"></span>Mold inspection<span class="services__sep"></span>Lead inspection<span class="services__sep"></span>Radon inspection</p>
      <p>Termite Inspection<span class="services__sep"></span>Infared Scan.</p>
      <div class="services__dash"></div>
      <p>and also we provide inspections for single family homes condos</p>
      <p>co-ops town-homes and commercial property</p>
    </div>
  </section>

</body>
</html>
```